Brindlemoor Realty information card

We need a 5x7 two-sided card to hand out at open houses and provide to our charitable partners for distribution. We are a local real estate group looking to add a "give back" component to our business. We are located in a coastal community and would like to incorporate that feel into our design. We are giving clients who use us the ability to designate 1 out of the 10 charitable organizations we partner with - and we will make a donation to that organization.

We included the 10 partner logos below - we envision them pretty small. Also included 2 photos of the "Brindlemoor" and our logo. Have fun.
Updates

Project Deadline Extended
Reason: We're out of town until Wednesday, May 17th.

Target Market(s)

home buyers & sellers

Industry/Entity Type

Real Estate

Font styles to use
Serif
Sans Serif

Colors

Designer to choose colors to be used in the design.

Requirements
Must have
• slogan & tagline - see attached text file
• Brindlemoor photo
Nice to have
• partner logos - small - maybe in circles?

```html
<!DOCTYPE html>
<html lang="en">
<head>
<meta charset="utf-8">
<title>Brindlemoor Realty – Information Card</title>
<link rel="stylesheet" href="https://fonts.googleapis.com/css2?family=Bebas+Neue&family=Montserrat:wght@400;500;700&display=swap">
<style>
  :root{
    --page:#e4e5e7;
    --paper:#f0f0f1;
    --blue:#1aa9e1;
    --deep-blue:#1d6cc6;
    --ink:#2a2b2e;
    --body:#3b3c40;
    --muted:#5a5c60;
    --band-top:#5c5f64;
    --band-bottom:#222428;
    --white:#ffffff;
    --url:#bfe6f7;
  }
  *{box-sizing:border-box;margin:0;padding:0}
  html,body{width:1200px;height:922px;overflow:hidden;background:var(--page)}
  .stage{position:relative;width:1200px;height:922px}
  .card{position:absolute;top:97px;width:520px;height:728px;background:var(--paper);overflow:hidden;box-shadow:0 6px 18px rgba(0,0,0,.18)}
  .card--front{left:60px}
  .card--back{left:620px}
  .card__art{position:absolute;inset:0;width:520px;height:728px}

  .headline{position:absolute;font-family:"Bebas Neue",sans-serif;font-weight:400;font-size:62px;line-height:1;letter-spacing:.5px;text-transform:uppercase}
  .headline span{display:block}
  .headline .accent{color:var(--blue)}
  .headline .dark{color:var(--ink)}

  .front-headline{left:30px;top:38px}
  .tagline{position:absolute;left:40px;top:430px;font-family:"Montserrat",sans-serif;font-weight:500;font-size:24px;line-height:1.3;color:var(--muted)}
  .front-copy{position:absolute;left:45px;top:505px;width:430px;font-family:"Montserrat",sans-serif;font-size:13.5px;line-height:1.45;color:var(--body);text-align:center}
  .fund-mark{position:absolute;left:204px;top:592px;width:112px;height:112px;border-radius:50%;display:flex;flex-direction:column;align-items:center;justify-content:center;font-family:"Montserrat",sans-serif;font-weight:700;font-size:16px;line-height:1.2;color:var(--white)}

  .back-headline{left:34px;top:40px}
  .back-rule{position:absolute;left:36px;top:178px;width:130px;height:4px;background:var(--blue)}
  .back-copy{position:absolute;left:36px;top:278px;width:452px;font-family:"Montserrat",sans-serif;font-size:12.2px;line-height:1.36;color:var(--body)}
  .back-copy p{margin-bottom:6px}
  .partners-label{position:absolute;left:56px;top:508px;font-family:"Montserrat",sans-serif;font-size:13px;color:var(--deep-blue)}

  .contact{position:absolute;font-family:"Montserrat",sans-serif;color:var(--white)}
  .contact__name{font-weight:700;font-size:16px;color:var(--blue);letter-spacing:.3px}
  .contact__mail{font-size:13px;margin-top:2px}
  .contact--left{left:34px;top:656px}
  .contact--right{right:30px;top:640px;text-align:right}
  .back-site{position:absolute;left:0;width:520px;top:698px;text-align:center;font-family:"Montserrat",sans-serif;font-weight:500;font-size:15px;color:var(--url);letter-spacing:.4px}
</style>
</head>
<body>
<main class="stage">

  <section class="card card--front" aria-label="Front side">
    <svg class="card__art" viewBox="0 0 520 728">
      <defs>
        <linearGradient id="sunset" x1="0" y1="0" x2="0" y2="1">
          <stop offset="0" stop-color="#f3a58c"/>
          <stop offset=".35" stop-color="#e9897c"/>
          <stop offset=".55" stop-color="#8f6f86"/>
          <stop offset=".8" stop-color="#3c344c"/>
          <stop offset="1" stop-color="#27243a"/>
        </linearGradient>
        <linearGradient id="bandFront" x1="0" y1="0" x2="0" y2="1">
          <stop offset="0" stop-color="#5c5f64"/>
          <stop offset="1" stop-color="#222428"/>
        </linearGradient>
      </defs>
      <polygon points="330,0 520,0 520,470" fill="#2b2e34"/>
      <polygon points="380,0 520,0 520,170" fill="#1aa9e1"/>
      <polygon points="410,0 500,0 455,62" fill="#1d6cc6"/>
      <polyline points="20,440 340,70 380,70" fill="none" stroke="#1aa9e1" stroke-width="1.5"/>
      <polygon role="img" aria-label="Photo of a coastal town at sunset with a pier reaching into the sea"
        points="60,400 360,120 520,320 520,480 430,390 350,420" fill="url(#sunset)"/>
      <polyline points="100,395 360,150 500,320" fill="none" stroke="#ffffff" stroke-opacity=".6" stroke-width="1.2"/>
      <polygon points="460,410 488,438 460,466 432,438" fill="#5cc3ea"/>
      <polygon points="0,622 260,682 520,606 520,728 0,728" fill="url(#bandFront)"/>
      <polyline points="0,610 260,670 520,590" fill="none" stroke="#1aa9e1" stroke-width="9"/>
      <circle cx="260" cy="648" r="56" fill="#2b2d31" stroke="#a3a5a9" stroke-width="5"/>
      <line x1="40" y1="712" x2="110" y2="712" stroke="#8a8c90" stroke-width="1"/>
      <line x1="410" y1="704" x2="480" y2="704" stroke="#8a8c90" stroke-width="1"/>
      <text x="260" y="718" text-anchor="middle" font-family="Montserrat, sans-serif" font-weight="500" font-size="14" fill="#bfe6f7">www.brindlemoorrealty.com</text>
      <rect x="0" y="722" width="520" height="6" fill="#1aa9e1"/>
    </svg>
    <h1 class="headline front-headline"><span class="accent">Change Homes</span><span class="dark">Change Lives</span></h1>
    <p class="tagline">Changing the World<br>One Home at a Time</p>
    <p class="front-copy">Because we value generosity and desire to make a difference in our community and world, for every home bought or sold through us, we will make a contribution to one of our amazing partner who are helping to change the world.</p>
    <div class="fund-mark"><span>Brindlemoor</span><span>Fund</span></div>
  </section>

  <section class="card card--back" aria-label="Back side">
    <svg class="card__art" viewBox="0 0 520 728">
      <defs>
        <linearGradient id="coast" x1="0" y1="0" x2="0" y2="1">
          <stop offset="0" stop-color="#cfe4f2"/>
          <stop offset=".4" stop-color="#8fbfdc"/>
          <stop offset=".6" stop-color="#8c8a7c"/>
          <stop offset=".85" stop-color="#5b6a4a"/>
          <stop offset="1" stop-color="#8a3b35"/>
        </linearGradient>
        <linearGradient id="bandBack" x1="0" y1="0" x2="0" y2="1">
          <stop offset="0" stop-color="#5c5f64"/>
          <stop offset="1" stop-color="#222428"/>
        </linearGradient>
      </defs>
      <polygon role="img" aria-label="Photo of the coastal town hillside overlooking the bay"
        points="240,220 400,40 520,40 520,220 470,258 430,228 400,248" fill="url(#coast)"/>
      <polygon points="280,110 330,60 345,130" fill="#9fd4ef" opacity=".8"/>
      <polyline points="225,232 420,20 500,20" fill="none" stroke="#1aa9e1" stroke-width="1.5"/>
      <polyline points="380,222 470,266 520,228" fill="none" stroke="#1aa9e1" stroke-width="1.5"/>
      <g fill="#d9dadc" stroke="#ffffff" stroke-width="2">
        <circle cx="160" cy="490" r="24"/><circle cx="222" cy="488" r="24"/><circle cx="284" cy="486" r="24"/><circle cx="346" cy="484" r="24"/><circle cx="408" cy="482" r="24"/>
        <circle cx="164" cy="544" r="24"/><circle cx="226" cy="542" r="24"/><circle cx="288" cy="540" r="24"/><circle cx="350" cy="538" r="24"/><circle cx="412" cy="536" r="24"/>
      </g>
      <polygon points="0,580 260,650 520,560 520,728 0,728" fill="url(#bandBack)"/>
      <polyline points="0,566 260,638 520,546" fill="none" stroke="#1aa9e1" stroke-width="9"/>
      <polygon points="232,640 288,640 260,656" fill="#1aa9e1"/>
      <line x1="40" y1="712" x2="110" y2="712" stroke="#8a8c90"/>
      <line x1="410" y1="712" x2="480" y2="712" stroke="#8a8c90"/>
    </svg>
    <h2 class="headline back-headline"><span class="accent">We Live Here.</span><span class="dark">We Give Here.</span></h2>
    <div class="back-rule"></div>
    <div class="back-copy">
      <p>We give because we value generosity and believe we have been blessed to be a blessing. We believe that together we can change the world one home at time.</p>
      <p>You have our guarantee of personal service and no additional costs. The donations come out of our commission, not your pocket. You get to designate which of our amazing partner organizations you would like us to contribute to on behalf of your transaction.</p>
      <p>When you are ready to buy or sell, please consider giving us a call. Tell a friend about us too. Together, we can make the world a better place.</p>
    </div>
    <p class="partners-label">Partners :</p>
    <div class="contact contact--left"><p class="contact__name">OWEN HARLOW</p><p class="contact__mail">owen@brindlemoorrealty.com</p></div>
    <div class="contact contact--right"><p class="contact__name">MARA HARLOW</p><p class="contact__mail">mara@brindlemoorrealty.com</p></div>
    <p class="back-site">www.brindlemoorrealty.com</p>
  </section>

</main>
</body>
</html>
```